FelixHarlan's Signature Beard Oil Label Design

I'm looking for a creative designer to run with the design. I am not sure what I really want so surprise me. What ever you do please use earth tone colors. The bottles I use is 2.0 ounces. It is a Boston amber bottle with glass dropper. It is 1.5 width by 3.75 inch height. :Benefits : * Organic * Hair growth* Repairs Split Ends* Softens * Health Shine* Aromatherapy fragrance* Reduce Itching/Irritation * Reduce Dandruff* Reduces Flyaway hair Directions: Place a nickel size drop into palm of handMassage into beard 2 to 3 times a day

Target Market(s)

MEN WITH BEARDS AND MEN THAT WANT TO GROW BEARDS BUT DON'T KNOW HOW

Industry/Entity Type

Hair Care Product

Font styles to use
Serif
Script

Colors
1b1b1b
fdf9cf
ffc214
ffffff

Requirements
Must have
• FALL COLOR SCHEME, Felix Harlan written in a fancy cursive script, all others can me different, please use the gold lion logo without the word Lion.
Nice to have
• CLASSY, MANLY, OLD AND NEW SCHOOL ESSENCE
Should not have
• Anything feminine, Pine Hollow

```html
<!DOCTYPE html>
<html lang="en">
<head>
<meta charset="utf-8">
<title>Felix Harlan Organic Beard Oil Label</title>
<link href="https://fonts.googleapis.com/css2?family=Mrs+Saint+Delafield&family=Old+Standard+TT&family=Playfair+Display:ital,wght@0,400;1,400&family=Roboto:wght@400;500&display=swap" rel="stylesheet">
<style>
  :root {
    --page: #c9cbcf;
    --label: #48484b;
    --ink: #ffffff;
    --ink-soft: #e3e3e3;
    --gold: #c8901c;
  }
  html, body {
    margin: 0;
    width: 1200px;
    height: 1200px;
    overflow: hidden;
    background: var(--page);
  }
  .label {
    position: absolute;
    left: 280px;
    top: 60px;
    width: 640px;
    height: 1080px;
    background: var(--label);
    color: var(--ink);
    text-align: center;
  }
  .arched-title {
    position: absolute;
    left: 0;
    top: 70px;
    width: 640px;
    height: 110px;
  }
  .arched-title text {
    font-family: "Old Standard TT", serif;
    font-size: 27px;
    letter-spacing: 4px;
    fill: var(--ink);
  }
  .est, .year {
    position: absolute;
    top: 176px;
    font-family: "Playfair Display", serif;
    font-size: 14px;
    line-height: 1;
    color: var(--gold);
  }
  .est { left: 196px; }
  .year { left: 392px; }
  .signature {
    position: absolute;
    top: 212px;
    font-family: "Mrs Saint Delafield", cursive;
    font-size: 66px;
    color: var(--ink);
    line-height: 1;
  }
  .signature.first { left: 70px; }
  .signature.last { left: 384px; }
  .brand-mark {
    position: absolute;
    left: 282px;
    top: 196px;
    width: 76px;
    height: 76px;
    border-radius: 50%;
    background: var(--gold);
  }
  .tagline {
    position: absolute;
    top: 316px;
    left: 0;
    width: 100%;
    font-family: "Old Standard TT", serif;
    font-size: 26px;
    letter-spacing: 5px;
  }
  .ornament {
    position: absolute;
    left: 82px;
    top: 410px;
    width: 476px;
    height: 128px;
    background: linear-gradient(180deg, rgba(227,227,227,0.15), rgba(227,227,227,0.55));
  }
  .dosage {
    position: absolute;
    top: 575px;
    left: 0;
    width: 100%;
    height: 110px;
  }
  .numero {
    position: absolute;
    left: 130px;
    top: 14px;
    font-family: "Roboto", sans-serif;
    font-weight: 500;
    font-size: 58px;
  }
  .numero-note {
    position: absolute;
    left: 160px;
    top: 82px;
    font-family: "Roboto", sans-serif;
    font-size: 11px;
  }
  .ratio {
    position: absolute;
    left: 212px;
    top: -6px;
    font-family: "Playfair Display", serif;
    font-style: italic;
    font-size: 104px;
    letter-spacing: 2px;
    line-height: 1.1;
  }
  .times {
    position: absolute;
    left: 384px;
    top: 6px;
    font-family: "Roboto", sans-serif;
    font-weight: 500;
    font-size: 42px;
    line-height: 1;
  }
  .daily {
    position: absolute;
    left: 384px;
    top: 52px;
    font-family: "Roboto", sans-serif;
    font-style: italic;
    font-size: 42px;
    color: var(--ink-soft);
    line-height: 1;
  }
  .direction {
    position: absolute;
    top: 690px;
    left: 0;
    width: 100%;
    margin: 0;
    font-family: "Playfair Display", serif;
    font-style: italic;
    font-size: 19px;
  }
  .direction-main {
    position: absolute;
    top: 728px;
    left: 0;
    width: 100%;
    margin: 0;
    font-family: "Roboto", sans-serif;
    font-weight: 500;
    font-size: 34px;
  }
  .benefits {
    position: absolute;
    top: 800px;
    left: 0;
    width: 100%;
    margin: 0;
    padding: 0;
    list-style: none;
    font-family: "Old Standard TT", serif;
    font-size: 22px;
    letter-spacing: 3.5px;
    line-height: 25px;
  }
</style>
</head>
<body>
  <main class="label">
    <svg class="arched-title" viewBox="0 0 640 110" aria-label="Organic Beard Oil">
      <path id="title-arc" d="M150 105 Q320 30 490 105" fill="none"/>
      <text><textPath href="#title-arc" startOffset="50%" text-anchor="middle">Organic Beard Oil</textPath></text>
    </svg>

    <span class="est">EST.</span>
    <span class="year">MMXVII</span>
    <span class="signature first">Felix</span>
    <span class="brand-mark" aria-hidden="true"></span>
    <span class="signature last">Harlan</span>

    <div class="tagline">Hair Growth</div>

    <div class="ornament" role="img" aria-label="Light grey moustache-shaped ornament"></div>

    <section class="dosage">
      <span class="numero">№</span>
      <span class="numero-note">of use</span>
      <span class="ratio">2/3</span>
      <span class="times">times</span>
      <span class="daily">daily</span>
    </section>

    <p class="direction">Place a nickel size drop into palm of hand</p>
    <p class="direction-main">Massage into beard</p>

    <ul class="benefits">
      <li>Reduces Dandruff &amp; Flyaway hair</li>
      <li>Softens</li>
      <li>Repairs Split Ends</li>
      <li>Reduce Itching/Irritation</li>
      <li>Health Shine</li>
      <li>Aromatherapy fragrance</li>
    </ul>
  </main>
</body>
</html>
```